YARD FRONTS "N" MORE

catyering to driveway/patio floor construction and remodeling. Concrete, concrete pavers, asphalt, Landscaping, irrigation, pergolas and pools.

Target Market(s)

the home owner that wants to enhance their home

Industry/Entity Type

construction

Contact Information for Business Card

presidet: tomas bellweather email: yardfrontsnmore@example.come office/cell: 555 214 8830

Font styles to use
Sans Serif

Requirements
Must have
• logo should pop out
Nice to have
• the logo should demonstrate that we do exteriors only

```html
<!DOCTYPE html>
<html lang="en">
<head>
<meta charset="utf-8">
<title>Yard Fronts "N" More — Business Card</title>
<link href="https://fonts.googleapis.com/css2?family=Montserrat:wght@400;600;700;800&display=swap" rel="stylesheet">
<style>
  :root {
    --backdrop: #1b1b1b;
    --card: #ffffff;
    --navy: #0b1a4a;
    --red: #a30f12;
    --rule: #0b1a4a;
  }
  * { margin: 0; padding: 0; box-sizing: border-box; }
  html, body {
    width: 1200px; height: 1200px; overflow: hidden;
    background: var(--backdrop);
    font-family: "Montserrat", Arial, sans-serif;
    color: var(--navy);
  }
  .stage { position: relative; width: 1200px; height: 1200px; }
  .card {
    position: absolute; top: 244px;
    width: 411px; height: 712px;
    background: var(--card);
  }
  .card--front { left: 167px; }
  .card--back { left: 622px; border: 1px solid #000; }

  .brand {
    position: absolute; left: 0; right: 0;
    display: flex; flex-direction: column; align-items: center;
    text-align: center;
  }
  .brand__mark { background: var(--red); }
  .brand__name {
    font-weight: 800; color: var(--navy);
    text-transform: uppercase; line-height: 1.05; letter-spacing: 0.5px;
    white-space: nowrap;
  }
  .card--front .brand { top: 232px; }
  .card--front .brand__mark { width: 96px; height: 96px; margin-bottom: 22px; }
  .card--front .brand__name { font-size: 46px; }
  .card--back .brand { top: 84px; }
  .card--back .brand__mark { width: 62px; height: 62px; margin-bottom: 14px; }
  .card--back .brand__name { font-size: 32px; }

  .contact {
    position: absolute; left: 52px; width: 307px;
    text-align: center;
  }
  .contact__label {
    font-size: 16px; font-weight: 400; letter-spacing: 0.3px;
    padding-bottom: 2px;
    border-bottom: 1px solid var(--rule);
    line-height: 1.1;
  }
  .contact__value { font-weight: 700; line-height: 1.2; white-space: nowrap; }
  .contact--name { top: 325px; }
  .contact--name .contact__value { font-size: 29px; margin-top: 9px; }
  .contact--phone { top: 469px; }
  .contact--phone .contact__value { font-size: 33px; margin-top: 8px; }
  .contact--email { top: 593px; }
  .contact--email .contact__value { font-size: 17.5px; margin-top: 3px; letter-spacing: -0.2px; }
</style>
</head>
<body>
<main class="stage">
  <section class="card card--front">
    <div class="brand">
      <span class="brand__mark" aria-hidden="true"></span>
      <p class="brand__name">Yard Fronts<br>"N" More</p>
    </div>
  </section>

  <section class="card card--back">
    <div class="brand">
      <span class="brand__mark" aria-hidden="true"></span>
      <p class="brand__name">Yard Fronts<br>"N" More</p>
    </div>

    <div class="contact contact--name">
      <p class="contact__label">presidet</p>
      <p class="contact__value">Tomas Bellweather</p>
    </div>
    <div class="contact contact--phone">
      <p class="contact__label">office/cell</p>
      <p class="contact__value">555 214 8830</p>
    </div>
    <div class="contact contact--email">
      <p class="contact__label">email</p>
      <p class="contact__value">yardfrontsnmore@example.come</p>
    </div>
  </section>
</main>
</body>
</html>
```